Upgrade Brenmoors

Hi,
We are an accounting firm looking to upgrade the following:
Logo, letterhead, withcomp slips and maybe our business cards. I have attached our original letterhead (sample A) and a letterhead (SAmple B) which we like the design and layout, however I want to stick with the colours of our orginal letterhead (Sample A) but improve and modernise the look with other letter head (Sample B) I have attached both. On the footer of Sample A, we would like to remove the names of the directors but leave EST. 1985 we also want to add the MDV logo ABN and TAX AGENT logo as stated in Sample B , we would like to do a layout for the header similar to SAmple B however maybe a bit more structured.

```html
<!DOCTYPE html>
<html lang="en">
<head>
<meta charset="utf-8">
<title>Brenmoors Accountants – Stationery</title>
<link href="https://fonts.googleapis.com/css2?family=Montserrat:wght@400;500;600;700&family=Arimo:wght@400;700&family=Tinos&family=Pinyon+Script&display=swap" rel="stylesheet">
<style>
  :root{
    --navy:#172b55;
    --blue:#3f8fd0;
    --ink:#1f1f1f;
    --paper:#ffffff;
    --backdrop:#e6e7e8;
    --lime:#9bc63b;
    --badge-grey:#8a8f96;
    --badge-orange:#e8763a;
  }
  *{margin:0;padding:0;box-sizing:border-box}
  html,body{width:1200px;height:1047px;overflow:hidden;background:var(--backdrop)}
  body{position:relative;font-family:"Montserrat",sans-serif;color:var(--ink)}
  .sprites{position:absolute;width:0;height:0}

  .sheet{position:absolute;background:var(--paper);overflow:hidden}
  .top-bar{position:absolute;left:0;top:0;width:100%;background:var(--navy)}
  .wave{position:absolute;left:0;bottom:0;width:100%}

  .brand{position:absolute;display:flex;align-items:center;gap:.3em;font-family:"Montserrat",sans-serif;font-weight:700;color:var(--navy);letter-spacing:-.01em;line-height:1}
  .brand .mark{width:.42em;height:.42em;background:var(--blue)}

  .contacts{position:absolute;list-style:none;line-height:1.45}
  .contacts li{display:flex;align-items:center;gap:.5em;white-space:nowrap}
  .contacts svg{width:1.15em;height:1.15em;fill:none;stroke:var(--ink);stroke-width:1.6}
  .contacts b{font-weight:700}
  .address{position:absolute;text-align:right;line-height:1.45;white-space:nowrap;font-style:normal}

  .legal{position:absolute;white-space:nowrap;line-height:1.2}
  .legal .firm{font-family:"Arimo",sans-serif;font-weight:700;display:flex}
  .legal .firm .firm-name{width:var(--abn-offset)}
  .legal .note{font-family:"Tinos",serif}
  .badge-square{position:absolute;background:var(--badge-orange);border-radius:12%;opacity:.85}
  .badge-circle{position:absolute;border-radius:50%;background:var(--lime);border:solid var(--badge-grey)}
  .agent{position:absolute;font-family:"Arimo",sans-serif;line-height:1.35;white-space:nowrap}
  .est{position:absolute;color:#fff;font-family:"Montserrat",sans-serif;font-weight:400;white-space:nowrap}

  /* letterhead */
  .letterhead{left:408px;top:61px;width:714px;height:925px}
  .letterhead .top-bar{height:15px}
  .letterhead .brand{left:48px;top:50px;font-size:30px}
  .letterhead .contacts{left:333px;top:40px;font-size:9px}
  .letterhead .address{right:34px;top:39px;font-size:9px}
  .letterhead .wave{height:112px}
  .letterhead .legal{left:35px;top:837px;--abn-offset:211px}
  .letterhead .legal .firm{font-size:9.3px}
  .letterhead .legal .note{font-size:9.5px}
  .letterhead .badge-square{left:388px;top:820px;width:30px;height:28px}
  .letterhead .badge-circle{left:464px;top:812px;width:60px;height:60px;border-width:2px}
  .letterhead .agent{left:535px;top:830px;font-size:9px}
  .letterhead .est{right:28px;top:891px;font-size:14px}

  /* compliments slip */
  .comp-slip{left:57px;top:477px;width:779px;height:366px}
  .comp-slip .top-bar{height:9px}
  .comp-slip .brand{left:30px;top:28px;font-size:21px}
  .comp-slip .greeting{position:absolute;left:30px;top:60px;font-family:"Pinyon Script",cursive;font-size:34px;color:var(--navy);white-space:nowrap}
  .comp-slip .contacts{left:560px;top:29px;font-size:5.4px}
  .comp-slip .address{right:20px;top:29px;font-size:5.4px}
  .comp-slip .wave{height:113px}
  .comp-slip .legal{left:38px;top:273px;--abn-offset:230px}
  .comp-slip .legal .firm{font-size:10.2px}
  .comp-slip .legal .note{font-size:10px}
  .comp-slip .badge-square{left:422px;top:251px;width:33px;height:30px}
  .comp-slip .badge-circle{left:507px;top:242px;width:65px;height:65px;border-width:2px}
  .comp-slip .agent{left:583px;top:262px;font-size:9.5px}
  .comp-slip .est{right:31px;top:318px;font-size:15px}

  /* business card front */
  .card-front{left:61px;top:53px;width:322px;height:185px}
  .card-front .brand{left:42px;top:20px;font-size:18px}
  .card-front .holder{position:absolute;right:37px;top:28px;text-align:right;line-height:1.05}
  .card-front .holder .name{font-size:16px;font-weight:500;color:var(--navy)}
  .card-front .holder .role{font-size:8px;color:var(--blue)}
  .card-front .contacts{left:32px;top:82px;font-size:5.8px}
  .card-front .address{right:36px;top:82px;font-size:5.8px}
  .card-front .wave{height:55px}
  .card-front .legal{left:16px;top:146px;--abn-offset:94px}
  .card-front .legal .firm{font-size:3.9px}
  .card-front .legal .note{font-size:3.6px}
  .card-front .badge-square{left:175px;top:139px;width:12px;height:11px}
  .card-front .badge-circle{left:210px;top:134px;width:25px;height:25px;border-width:1px}
  .card-front .agent{left:240px;top:142px;font-size:3.6px}
  .card-front .est{right:12px;top:166px;font-size:6.5px}

  /* business card back */
  .card-back{left:59px;top:256px;width:323px;height:185px;background:var(--navy)}
  .card-back .pattern{position:absolute;inset:0;background:linear-gradient(135deg,#1b3061,#152850)}
  .card-back .brand{left:50%;top:50%;transform:translate(-50%,-50%);font-size:26px;color:#fff}
  .card-back .brand .mark{background:#fff}
</style>
</head>
<body>

<svg class="sprites" aria-hidden="true">
  <symbol id="icon-phone" viewBox="0 0 16 16"><path d="M2 6c0-2 3-3.5 6-3.5S14 4 14 6l-2.5.5-.5-1.5H5l-.5 1.5z"/><rect x="3" y="8" width="10" height="6" rx="1"/><circle cx="8" cy="11" r="1.3"/></symbol>
  <symbol id="icon-fax" viewBox="0 0 16 16"><rect x="4" y="1.5" width="8" height="5"/><rect x="1.5" y="6.5" width="13" height="8" rx="1"/><path d="M4 9.5h2M7 9.5h2M10 9.5h2M4 12h2M7 12h2M10 12h2"/></symbol>
  <symbol id="icon-mail" viewBox="0 0 16 16"><rect x="1.5" y="3" width="13" height="10"/><path d="M1.5 3 8 9l6.5-6M1.5 13 6.5 7.5M14.5 13 9.5 7.5"/></symbol>
  <symbol id="icon-web" viewBox="0 0 16 16"><circle cx="8" cy="8" r="6.5"/><ellipse cx="8" cy="8" rx="2.8" ry="6.5"/><path d="M1.5 8h13M2.5 4.8h11M2.5 11.2h11"/></symbol>
  <symbol id="footer-wave" viewBox="0 0 1224 190" preserveAspectRatio="none">
    <path fill="#172b55" d="M0 150C420 195 830 150 1224 10V190H0Z"/>
    <path fill="#3f8fd0" d="M0 103C360 150 760 158 1010 82 760 168 380 182 0 150Z"/>
  </symbol>
</svg>

<!-- Letterhead -->
<section class="sheet letterhead">
  <div class="top-bar"></div>
  <div class="brand"><span class="mark"></span>Brenmoors</div>
  <ul class="contacts">
    <li><svg><use href="#icon-phone"/></svg>+61 3 <b>9012 4470</b></li>
    <li><svg><use href="#icon-fax"/></svg>+61 3 <b>9012 4471</b></li>
    <li><svg><use href="#icon-mail"/></svg>info@brenmoors.com.au</li>
    <li><svg><use href="#icon-web"/></svg>www.brenmoorsaccountants.com.au</li>
  </ul>
  <address class="address">Brenmoors Pty Ltd<br>ABN 52 310 774 908<br>220 Park Road<br>Kew Vic. 3101</address>
  <svg class="wave" preserveAspectRatio="none"><use href="#footer-wave"/></svg>
  <div class="legal">
    <p class="firm"><span class="firm-name">Northvale Accountants (MEL) Pty Limited</span><span>ABN 41 227 906 518</span></p>
    <p class="note">Liability limited by a scheme approved under Professional Standards Legislation</p>
  </div>
  <div class="badge-square" role="img" aria-label="Professional membership badge"></div>
  <div class="badge-circle" role="img" aria-label="Registered tax agent badge"></div>
  <p class="agent">Text Agent<br>48120376</p>
  <p class="est">EST. 1985</p>
</section>

<!-- Business card back -->
<section class="sheet card-back">
  <div class="pattern" role="img" aria-label="Subtle navy geometric pattern"></div>
  <div class="brand"><span class="mark"></span>Brenmoors</div>
</section>

<!-- Business card front -->
<section class="sheet card-front">
  <div class="brand"><span class="mark"></span>Brenmoors</div>
  <div class="holder"><p class="name">Alex Reid</p><p class="role">Founder</p></div>
  <ul class="contacts">
    <li><svg><use href="#icon-phone"/></svg>+61 3 <b>9012 4470</b></li>
    <li><svg><use href="#icon-fax"/></svg>+61 3 <b>9012 4471</b></li>
    <li><svg><use href="#icon-mail"/></svg>info@brenmoors.com.au</li>
    <li><svg><use href="#icon-web"/></svg>www.brenmoorsaccountants.com.au</li>
  </ul>
  <address class="address">Brenmoors Pty Ltd<br>ABN 52 310 774 908<br>220 Park Road<br>Kew Vic. 3101</address>
  <svg class="wave" preserveAspectRatio="none"><use href="#footer-wave"/></svg>
  <div class="legal">
    <p class="firm"><span class="firm-name">Northvale Accountants (MEL) Pty Limited</span><span>ABN 41 227 906 518</span></p>
    <p class="note">Liability limited by a scheme approved under Professional Standards Legislation</p>
  </div>
  <div class="badge-square" role="img" aria-label="Professional membership badge"></div>
  <div class="badge-circle" role="img" aria-label="Registered tax agent badge"></div>
  <p class="agent">Text Agent<br>48120376</p>
  <p class="est">EST. 1985</p>
</section>

<!-- Compliments slip -->
<section class="sheet comp-slip">
  <div class="top-bar"></div>
  <div class="brand"><span class="mark"></span>Brenmoors</div>
  <p class="greeting">With Compliments</p>
  <ul class="contacts">
    <li><svg><use href="#icon-phone"/></svg>+61 3 <b>9012 4470</b></li>
    <li><svg><use href="#icon-fax"/></svg>+61 3 <b>9012 4471</b></li>
    <li><svg><use href="#icon-mail"/></svg>info@brenmoors.com.au</li>
    <li><svg><use href="#icon-web"/></svg>www.brenmoorsaccountants.com.au</li>
  </ul>
  <address class="address">Brenmoors Pty Ltd<br>ABN 52 310 774 908<br>220 Park Road<br>Kew Vic. 3101</address>
  <svg class="wave" preserveAspectRatio="none"><use href="#footer-wave"/></svg>
  <div class="legal">
    <p class="firm"><span class="firm-name">Northvale Accountants (MEL) Pty Limited</span><span>ABN 41 227 906 518</span></p>
    <p class="note">Liability limited by a scheme approved under Professional Standards Legislation</p>
  </div>
  <div class="badge-square" role="img" aria-label="Professional membership badge"></div>
  <div class="badge-circle" role="img" aria-label="Registered tax agent badge"></div>
  <p class="agent">Text Agent<br>48120376</p>
  <p class="est">EST. 1985</p>
</section>

</body>
</html>
```